Brightpath Desk letterhead and envelope

Design a formal (8.5x11) letterhead and envelope for sales outreach and legal matters. Using design input from https://www.brightpathdesk.com/ and the attached documents.

Industry/Entity Type

Software Service

Requirements
Must have
• These 4 hex colors are our official colors:
• #355c98 [blue]
• #1eb1a2 [teal]
• #fdba12 [gold]
• #f1653b [orange]
• So no other colors besides these should be used.

```html
<!DOCTYPE html>
<html lang="en">
<head>
<meta charset="utf-8">
<title>Brightpath Desk Stationery</title>
<link href="https://fonts.googleapis.com/css2?family=Roboto:wght@300;400;500&display=swap" rel="stylesheet">
<style>
  :root{
    --blue:#355c98;
    --teal:#1eb1a2;
    --gold:#fdba12;
    --orange:#f1653b;
    --paper:#f0f0f0;
    --ink:#6b6b6b;
    --ink-dark:#333;
    --backdrop:#e4e4e4;
  }
  *{margin:0;padding:0;box-sizing:border-box}
  html,body{width:1200px;height:946px;overflow:hidden}
  body{background:var(--backdrop);font-family:'Roboto',sans-serif;position:relative}
  .sheet{position:absolute;background:var(--paper)}
  .band{position:absolute;left:0;right:0;bottom:0;background:var(--blue)}
  .wordmark{position:absolute;display:flex;align-items:center;gap:8px;color:var(--blue);font-weight:300;white-space:nowrap}
  .wordmark .dot{border:2px solid var(--blue);border-radius:50%;flex:none}

  /* Letterhead */
  .letterhead{left:107px;top:148px;width:478px;height:671px}
  .letterhead .band{height:16px}
  .letterhead .wordmark{left:31px;top:43px;font-size:25px}
  .letterhead .wordmark .dot{width:30px;height:30px}
  .contact{position:absolute;font-size:8px;line-height:11px}
  .contact.direct{left:261px;top:46px;color:var(--ink-dark);font-weight:500}
  .contact.office{left:373px;top:46px;color:var(--ink)}
  .divider{position:absolute;left:362px;top:46px;width:1px;height:30px;background:#aaa}
  .recipient{position:absolute;left:43px;top:200px;font-size:8.5px;line-height:12.5px;color:var(--ink)}
  .body-copy{position:absolute;left:43px;width:396px;font-size:8.2px;line-height:12.4px;color:var(--ink);text-align:justify}
  .body-copy.p1{top:274px}
  .body-copy.p2{top:386px}
  .signature{position:absolute;left:43px;top:460px;width:92px;height:60px;background:linear-gradient(135deg,#e6e6e6,#d9d9d9);border-radius:4px}
  .sign-title{position:absolute;left:43px;top:532px;font-size:8.5px;color:var(--ink)}

  /* Envelope back */
  .envelope-back{left:630px;top:314px;width:475px;height:237px}
  .flap{position:absolute;left:0;top:0;width:475px;height:72px}
  .flap-name{position:absolute;left:0;right:0;top:22px;text-align:center;font-size:16px;font-weight:300;color:var(--blue)}

  /* Envelope front */
  .envelope-front{left:629px;top:584px;width:475px;height:236px}
  .envelope-front .band{height:15px}
  .envelope-front .wordmark{left:24px;top:30px;font-size:18px}
  .envelope-front .wordmark .dot{width:22px;height:22px}
  .envelope-front .contact{font-size:7.3px;line-height:10.5px}
  .envelope-front .contact.direct{left:25px;top:81px}
  .envelope-front .contact.office{left:25px;top:118px}
</style>
</head>
<body>

<section class="sheet letterhead">
  <div class="wordmark"><span class="dot"></span>Brightpath Desk</div>
  <div class="contact direct">(555) 014-2290<br>jsmith@brightpathdesk.com<br>www.brightpathdesk.com</div>
  <div class="divider"></div>
  <div class="contact office">Main: (555) 017-4406<br>82 Linden Row<br>Fairview, OR 97000</div>

  <div class="recipient">Dear Marlowe<br>Northgate Print Works<br>Department Design</div>

  <p class="body-copy p1">Lorem ipsum dolor sit amet, consectetuer adipiscing elit. Aenean commodo ligula eget dolor. Aenean massa. Cum sociis natoque penatibus et magnis dis parturient montes, nascetur ridiculus mus. Donec quam felis, ultricies nec, pellentesque eu, pretium quis, sem. Nulla consequat massa quis enim. Donec pede justo, fringilla vel, aliquet nec, vulputate eget, arcu. In enim justo, rhoncus ut, imperdiet a, venenatis vitae, justo. Nullam dictum felis eu pede mollis pretium. Integer tincidunt. Cras dapibus. Vivamus elementum semper nisi. Nullam dictum felis eu pede mollis pretium. Integer tincidunt. Cras dapibus. Vivamus elementum semper nisi. felis eu pede mollis pretium. Integer tincidunt. Cras dapibus.</p>
  <p class="body-copy p2">Quisque rutrum. Aenean imperdiet. Etiam ultricies nisi vel augue. Curabitur ullamcorper ultricies nisi. Nam eget dui. Etiam rhoncus. Maecenas tempus, tellus eget condimentum rhoncus, sem quam semper libero, sit amet adipiscing sem neque sed ipsum. felis pede mollis pretium. Integer tincidunt. Cras dapibus.</p>

  <div class="signature" role="img" aria-label="Handwritten signature of the director"></div>
  <div class="sign-title">Director/Executive Director</div>

  <div class="band"></div>
</section>

<section class="sheet envelope-back">
  <svg class="flap" viewBox="0 0 475 72" role="img" aria-label="Envelope flap with scattered pattern of small icons in teal, gold and orange">
    <defs>
      <linearGradient id="flapTone" x1="0" y1="0" x2="1" y2="0">
        <stop offset="0" stop-color="#f3e6e0"/>
        <stop offset="0.5" stop-color="#f1ebe4"/>
        <stop offset="1" stop-color="#e6eeec"/>
      </linearGradient>
    </defs>
    <path d="M0 0 H475 L467 56 Q465 70 450 70 H25 Q10 70 8 56 Z" fill="url(#flapTone)" stroke="#d6d6d6" stroke-width="0.8"/>
  </svg>
  <div class="flap-name">Brightpath Desk</div>
</section>

<section class="sheet envelope-front">
  <div class="wordmark"><span class="dot"></span>Brightpath Desk</div>
  <div class="contact direct">(555) 014-2290<br>jsmith@brightpathdesk.com<br>brightpathdesk.com</div>
  <div class="contact office">Main: (555) 017-4406<br>82 Linden Row<br>Fairview, OR 97000</div>
  <div class="band"></div>
</section>

</body>
</html>
```